hotel's Website

Hotels website redesign for reference pictures, logo etc see http://restwellmarlow.co.uk/

1. 2-3 Special offers on the main page.
2. Booking calender
3. Location Map
4. Picture gallery.
5. Journeyscope reviews.
6. short description
7. Social Media sharing.
8 Phone number and address.

Industry/Entity Type

Hotel

Requirements
Must have
• 1. 2-3 Special offers on the main page.
2. Booking calender
3. Location Map
4. Picture gallery.
5. Journeyscope reviews.
6. short description
7. Social Media sharing.

```html
<!DOCTYPE html>
<html lang="en">
<head>
<meta charset="utf-8">
<title>Restwell Inn – London Victoria</title>
<link href="https://fonts.googleapis.com/css2?family=Open+Sans:wght@400;600;700&family=PT+Sans+Narrow:wght@400;700&display=swap" rel="stylesheet">
<style>
:root{
  --blue:#1565ad;
  --blue-bright:#1a7bc8;
  --blue-dark:#0f4f8a;
  --orange:#e9a020;
  --ink:#333;
  --body:#444;
  --light:#f4f4f4;
  --rule:#c9c9c9;
  --white:#fff;
}
*{box-sizing:border-box;margin:0;padding:0}
html,body{width:1200px;height:1104px;overflow:hidden}
body{position:relative;font-family:"Open Sans",sans-serif;color:var(--body);background:var(--white)}
.abs{position:absolute}
.topbar{left:0;top:0;width:1200px;height:58px;background:var(--blue)}
.nav{display:flex;font-size:11px;color:var(--white);white-space:nowrap}
.nav span{padding:0 8px;border-left:1px solid rgba(255,255,255,.45);line-height:11px}
.nav span:first-child{padding-left:0;border-left:none}
.topbar .nav{left:201px;top:22px}
.social{left:944px;top:5px;display:flex;gap:5px}
.social i{width:15px;height:15px;border-radius:50%;background:var(--white);display:block;border:4px solid var(--white);box-shadow:inset 0 0 0 8px #e6eef7}
.translate{left:857px;top:36px;width:142px;height:13px;background:var(--white);display:flex;align-items:center;gap:3px;padding:0 4px;font-size:8px;letter-spacing:1px;color:#555}
.translate b{width:8px;height:7px;background:#c33;display:block}
.translate b.alt{background:#333}
.hero{left:0;top:58px;width:1200px;height:286px;background:
  radial-gradient(ellipse 420px 180px at 420px 230px,#ffffff 0%,rgba(255,255,255,0) 100%),
  radial-gradient(ellipse 90px 120px at 1080px 250px,#8a6a3e 0%,rgba(138,106,62,0) 100%),
  linear-gradient(90deg,#c9d6e0 0%,#e4e9ee 14%,#f3f3f1 30%,#f1efea 60%,#ece4d6 82%,#e2d3b8 100%)}
.brand{left:200px;top:68px;width:76px;height:88px;background:var(--blue);display:flex;align-items:center;justify-content:center;text-align:center;color:var(--white);font-size:13px;font-weight:600;line-height:15px}
.place{left:290px;top:103px;font-size:14px;color:#444;letter-spacing:.3px}
.dots{left:200px;top:328px;display:flex;gap:1px}
.dots i{width:10px;height:10px;background:#333;display:block}
.blue-line{left:0;top:343px;width:1200px;height:3px;background:var(--blue)}
.welcome{left:0;top:346px;width:1200px;height:184px;background:var(--orange)}
.welcome h1{position:absolute;left:201px;top:26px;font-family:"PT Sans Narrow",sans-serif;font-weight:700;font-size:42px;color:var(--ink);letter-spacing:-1px}
.welcome p{position:absolute;left:201px;top:86px;width:505px;font-size:10.3px;line-height:14.4px;color:#4a3a18}
.booking{left:728px;top:218px;width:270px;height:316px;background:var(--white);border-radius:8px 8px 0 0;box-shadow:0 0 4px rgba(0,0,0,.25)}
.booking .title{position:absolute;left:87px;top:12px;font-family:"PT Sans Narrow",sans-serif;font-weight:700;font-size:20px;color:var(--blue-bright);letter-spacing:-.3px}
.booking svg.icon{position:absolute;left:48px;top:5px}
.booking .rule{position:absolute;left:16px;top:41px;width:238px;height:4px;border-top:1px solid #9cc3e6;border-bottom:1px solid #9cc3e6}
.booking label{position:absolute;left:19px;font-size:9.5px;font-weight:700;color:var(--blue-bright)}
.field{position:absolute;border:1px solid #c9c9c9;border-radius:3px;font-size:9.5px;color:#555;display:flex;align-items:center;box-shadow:0 2px 3px rgba(0,0,0,.08)}
.field.wide{left:16px;width:246px;height:29px;padding-left:20px}
.field.small{top:197px;width:79px;height:28px;justify-content:center}
.search{position:absolute;left:54px;top:253px;width:160px;height:42px;background:var(--blue);border-radius:2px;color:var(--white);font-family:"PT Sans Narrow",sans-serif;font-weight:700;font-size:15px;display:flex;align-items:center;justify-content:center;letter-spacing:.3px}
.offers-band{left:0;top:530px;width:1200px;height:238px;background:var(--light)}
h2{position:absolute;font-family:"PT Sans Narrow",sans-serif;font-weight:400;font-size:22px;color:var(--ink);letter-spacing:-.5px;white-space:nowrap}
.photo{position:absolute;border:2px solid #cfcfcf}
.room-warm{background:radial-gradient(ellipse 60% 45% at 60% 75%,#efe6d8 0%,rgba(239,230,216,0) 100%),linear-gradient(90deg,#6b5130 0%,#a8864f 30%,#c8b38c 55%,#7d5e3c 100%)}
.room-night{background:radial-gradient(ellipse 55% 50% at 70% 40%,#3b3a34 0%,rgba(59,58,52,0) 100%),linear-gradient(90deg,#7a5a1e 0%,#c3962e 35%,#a07a2a 65%,#5c4518 100%)}
.room-soft{background:radial-gradient(ellipse 55% 40% at 55% 78%,#f3ebe0 0%,rgba(243,235,224,0) 100%),linear-gradient(90deg,#8a6a48 0%,#cdb79a 35%,#e2d3c1 60%,#a48866 100%)}
.person{background:radial-gradient(ellipse 50% 60% at 50% 50%,#f6f6f6 0%,#d7dce0 100%)}
.caption{position:absolute;font-size:9px;line-height:12.5px;color:#444}
.vrule{position:absolute;border-left:1px dotted #aaa}
.review-title{position:absolute;font-size:11.5px;font-weight:600;color:var(--blue-bright)}
.readmore{position:absolute;font-size:9.5px;font-style:italic;color:var(--blue-bright)}
.hrule{position:absolute;border-top:1px dotted #aaa}
.overlay{position:absolute;left:0;top:0;width:100%;height:100%;background:rgba(40,40,40,.55);color:var(--white);font-size:8.5px;line-height:11.5px;padding:8px 9px}
.map{background:radial-gradient(ellipse 50% 45% at 60% 65%,#f1e3c2 0%,rgba(241,227,194,0) 100%),linear-gradient(135deg,#dfe3c9 0%,#ece6cf 45%,#d8e2c4 100%)}
.address{position:absolute;left:748px;top:973px;font-size:8.8px;line-height:12.6px;color:#333}
.footer{left:0;top:1040px;width:1200px;height:64px;background:var(--blue)}
.footer .nav{left:201px;top:13px;color:#cfe0f2}
.footer .nav span{border-left-color:rgba(255,255,255,.35)}
.copy{left:201px;top:45px;font-size:8.8px;color:#cfe0f2}
.footer .brand{left:826px;top:4px;width:46px;height:54px;font-size:9px;line-height:11px;border:1px solid rgba(255,255,255,.6)}
.footer .place{left:883px;top:23px;color:var(--white);font-size:14px}
</style>
</head>
<body>

<header class="abs topbar">
  <nav class="abs nav"><span>HOME</span><span>OUR ROOMS</span><span>ATTRACTIONS</span><span>LONDON EVENTS</span><span>SPECIAL OFFER</span><span>PHOTOS</span><span>DIRECTIONS</span><span>CONTACT</span></nav>
  <div class="abs social" aria-label="Social sharing"><i></i><i></i><i></i></div>
  <div class="abs translate"><b></b><b class="alt"></b><span>TRANSLATE</span><b class="alt"></b><b></b></div>
</header>

<section class="abs hero" role="img" aria-label="Bright hotel bedroom with white bedding and a bedside lamp"></section>
<div class="abs brand">Restwell<br>Inn</div>
<div class="abs place">London &nbsp;-&nbsp; Victoria</div>
<div class="abs dots"><i></i><i></i><i></i><i></i></div>
<div class="abs blue-line"></div>

<section class="abs welcome">
  <h1>WELCOME</h1>
  <p>Lorem ipsum dolor sit amet, consectetuer adipiscing elit, sed diam nonummy nibh euismod tincidunt ut laoreet dolore magna aliquam erat volutpat. Ut wisi enim ad minim veniam, quis nostrud exerci tation ullamcorper suscipit lobortis nisl ut aliquip ex ea commodo consequat. Duis autem vel eum iriure dolor in hendrerit in vulputate velit esse molestie consequa.</p>
</section>

<aside class="abs booking">
  <svg class="icon" width="36" height="40" viewBox="0 0 36 40">
    <rect x="5" y="5" width="26" height="32" rx="3" fill="#1a7bc8" transform="rotate(-12 18 21)"/>
    <rect x="13" y="2" width="10" height="6" rx="2" fill="#0f4f8a" transform="rotate(-12 18 21)"/>
    <g stroke="#fff" stroke-width="2" transform="rotate(-12 18 21)"><line x1="10" y1="15" x2="26" y2="15"/><line x1="10" y1="21" x2="26" y2="21"/><line x1="10" y1="27" x2="26" y2="27"/></g>
  </svg>
  <div class="title">BOOK NOW</div>
  <div class="rule"></div>
  <label style="top:54px">FROM</label>
  <div class="field wide" style="top:68px">November 02, 2013</div>
  <label style="top:118px">TO</label>
  <div class="field wide" style="top:135px;padding-left:22px">November 04, 2013</div>
  <div class="field small" style="left:16px">Rooms</div>
  <div class="field small" style="left:99px">Adult</div>
  <div class="field small" style="left:183px">Children</div>
  <div class="search">SEARCH AVAILBILTY</div>
</aside>

<section class="abs offers-band"></section>
<h2 style="left:201px;top:556px">SPECIAL OFFERS</h2>
<div class="photo room-warm" style="left:201px;top:598px;width:159px;height:73px" role="img" aria-label="Twin room with warm wood panelling"></div>
<div class="photo room-soft" style="left:365px;top:598px;width:159px;height:73px" role="img" aria-label="Double room with striped walls"></div>
<div class="photo room-night" style="left:530px;top:598px;width:159px;height:73px" role="img" aria-label="Room with city view at night"></div>
<p class="caption" style="left:203px;top:691px">Lorem ipsum dolor sit amet,<br>consectetuer adipiscing elit, sed...</p>
<p class="caption" style="left:367px;top:691px">Lorem ipsum dolor sit amet,<br>consectetuer adipiscing elit, sed...</p>
<p class="caption" style="left:533px;top:691px">Lorem ipsum dolor sit amet,<br>consectetuer adipiscing elit, sed...</p>

<div class="vrule" style="left:724px;top:588px;height:148px"></div>
<h2 style="left:738px;top:556px">JOURNEYSCOPE REVIEWS</h2>
<div class="photo person" style="left:747px;top:598px;width:71px;height:47px" role="img" aria-label="Guest review photo"></div>
<div class="review-title" style="left:824px;top:596px">Lorem ipsum dolor</div>
<p class="caption" style="left:825px;top:612px">Lorem ipsum dolor sit amet,<br>consectetuer adipiscing elit, sed...</p>
<div class="readmore" style="left:953px;top:640px">Readmore</div>
<div class="hrule" style="left:738px;top:663px;width:260px"></div>
<div class="photo person" style="left:748px;top:680px;width:71px;height:47px" role="img" aria-label="Guest review photo"></div>
<div class="review-title" style="left:825px;top:675px">Lorem ipsum dolor</div>
<p class="caption" style="left:826px;top:691px">Lorem ipsum dolor sit amet,<br>consectetuer adipiscing elit, sed...</p>
<div class="readmore" style="left:947px;top:722px">Readmore</div>

<h2 style="left:201px;top:790px">PICTURE GALLERY</h2>
<div class="photo room-warm" style="left:199px;top:841px;width:161px;height:73px" role="img" aria-label="Twin room gallery photo">
  <div class="overlay">Enjoy your stay at Restwell Inn Victoria and be sure that you've found our best value on the Internet.</div>
</div>
<div class="photo room-warm" style="left:373px;top:841px;width:159px;height:73px" role="img" aria-label="Twin room gallery photo"></div>
<div class="photo room-night" style="left:545px;top:841px;width:160px;height:73px" role="img" aria-label="Room at night gallery photo"></div>
<div class="photo room-warm" style="left:199px;top:928px;width:160px;height:73px" role="img" aria-label="Twin room gallery photo"></div>
<div class="photo room-night" style="left:373px;top:928px;width:159px;height:73px" role="img" aria-label="City view room gallery photo"></div>
<div class="photo room-soft" style="left:545px;top:928px;width:160px;height:73px" role="img" aria-label="Double room gallery photo"></div>

<div class="vrule" style="left:726px;top:836px;height:164px;border-left-style:solid;border-color:#ddd"></div>
<h2 style="left:747px;top:790px">LOCATION MAP</h2>
<div class="photo map" style="left:747px;top:841px;width:253px;height:128px;border-width:1px" role="img" aria-label="Street map of central London showing the hotel location"></div>
<p class="address">42 HARROW LANE, VICTORIA LONDON SW1V 9ZX<br>STAY@RESTWELLMARLOW.CO.UK<br>TEL: + 44 (0) 20 7946 0123 | FAX:+ 44 (0) 20 7946 0456</p>

<footer class="abs footer">
  <nav class="abs nav"><span>HOME</span><span>OUR ROOMS</span><span>ATTRACTIONS</span><span>LONDON EVENTS</span><span>SPECIAL OFFER</span><span>PHOTOS</span><span>DIRECTIONS</span><span>CONTACT</span></nav>
  <div class="abs copy">Copyright © 2013 All rights reserved</div>
  <div class="abs brand">Restwell<br>Inn</div>
  <div class="abs place">London &nbsp;-&nbsp; Victoria</div>
</footer>

</body>
</html>
```